Tervolan Pty Ltd professional business card

A professional business card template using the colours from the supplied logo.
Clean crisp lines while, Modern while not being over the top.

Target Market(s)

Construction, commerical and industrial

Industry/Entity Type

Communications

Contact Information for Business Card

For a Communications, IT, Optical fibre installation company

Colors
37b8a4

```html
<!DOCTYPE html>
<html lang="en">
<head>
<meta charset="utf-8">
<title>Tervolan Pty Ltd – Business Card</title>
<link rel="stylesheet" href="https://fonts.googleapis.com/css2?family=Open+Sans:wght@400;600;700&family=Montserrat:wght@800&display=swap">
<style>
  :root {
    --teal: #27bba5;
    --teal-soft: #3fc6b0;
    --grey: #6d6e71;
    --grey-line: #8a8b8e;
    --white: #ffffff;
    --backdrop: #e9ecee;
  }
  * { box-sizing: border-box; margin: 0; padding: 0; }
  html, body { width: 1200px; height: 1000px; overflow: hidden; }
  body {
    background: var(--backdrop);
    font-family: "Open Sans", Arial, sans-serif;
    position: relative;
  }
  .card {
    position: absolute;
    left: 280px;
    width: 640px;
    height: 366px;
    border-radius: 16px;
    overflow: hidden;
    box-shadow: 0 6px 18px rgba(0,0,0,0.12);
  }
  /* Back side */
  .card-back { top: 92px; background: var(--teal); }
  .card-back .brand {
    position: absolute; left: 0; right: 0; top: 128px;
    text-align: center;
    font-weight: 600; font-size: 70px; letter-spacing: 4px;
    color: var(--white);
  }
  .card-back .web {
    position: absolute; left: 0; right: 0; top: 296px;
    text-align: center; font-size: 15px; letter-spacing: 1px;
    color: var(--white);
  }
  /* Front side */
  .card-front { top: 518px; background: var(--white); }
  .card-front .wave { position: absolute; inset: 0; }
  .card-front .brand {
    position: absolute; left: 40px; top: 118px;
    font-weight: 600; font-size: 44px; letter-spacing: 2px;
    color: var(--grey);
  }
  .card-front .divider {
    position: absolute; left: 328px; top: 70px;
    width: 1px; height: 160px; background: var(--grey-line);
    transform: rotate(12deg);
  }
  .contact { position: absolute; left: 362px; top: 74px; color: var(--grey); }
  .contact .name {
    font-family: "Montserrat", Arial, sans-serif; font-weight: 800;
    font-size: 21px; letter-spacing: 1.5px; color: var(--teal);
  }
  .contact .role { font-size: 14px; margin-bottom: 6px; }
  .contact .line { font-size: 14px; line-height: 20px; display: flex; align-items: center; gap: 6px; }
  .contact .icon { width: 11px; height: 11px; flex: none; }
</style>
</head>
<body>

  <section class="card card-back" aria-label="Card back">
    <div class="brand">TERVOLAN</div>
    <div class="web">www.tervolan.com.au</div>
  </section>

  <section class="card card-front" aria-label="Card front">
    <svg class="wave" viewBox="0 0 640 366" preserveAspectRatio="none" aria-hidden="true">
      <path d="M0,198 C180,270 420,330 640,340 L640,366 L0,366 Z" fill="var(--teal)"/>
      <path d="M30,208 C210,285 430,332 620,338" fill="none" stroke="var(--white)" stroke-width="5"/>
      <path d="M40,200 C220,282 440,330 620,334" fill="none" stroke="var(--grey)" stroke-width="3"/>
    </svg>

    <div class="brand">TERVOLAN</div>
    <div class="divider"></div>

    <div class="contact">
      <div class="name">MARLA QUENTIS</div>
      <div class="role">General Manager</div>
      <div class="line">14 Harlowmere Ave</div>
      <div class="line">Eastbrook, CT 551870</div>
      <div class="line">
        <svg class="icon" viewBox="0 0 12 12" aria-hidden="true"><path d="M2.5 1 L4.5 1 L5.2 3.5 L4 4.5 C4.6 5.8 5.9 7.2 7.4 7.9 L8.5 6.8 L11 7.5 L11 9.5 C11 10.4 10.3 11 9.5 11 C5 10.7 1.3 7 1 2.5 C1 1.7 1.6 1 2.5 1 Z" fill="var(--teal)"/></svg>
        (555) 014-2376
      </div>
      <div class="line">
        <svg class="icon" viewBox="0 0 12 12" aria-hidden="true"><rect x="0.5" y="2" width="11" height="8" fill="var(--teal)"/><path d="M0.5 2 L6 6.5 L11.5 2" fill="none" stroke="var(--white)" stroke-width="1"/></svg>
        contact@tervolan.com.au
      </div>
      <div class="line">
        <svg class="icon" viewBox="0 0 12 12" aria-hidden="true"><circle cx="6" cy="6" r="5" fill="none" stroke="var(--teal)" stroke-width="1.3"/><path d="M1 6 H11 M6 1 C3.5 4 3.5 8 6 11 M6 1 C8.5 4 8.5 8 6 11" fill="none" stroke="var(--teal)" stroke-width="1"/></svg>
        www.tervolan.com.au
      </div>
    </div>
  </section>

</body>
</html>
```